a promotional poster design to promote our upcoming event. We want the date to be promoted as "Save the Date" for Sunday 4th July 2021.

Poster design

Requirements
Must have
• the following text;

Save the Date! (stand out)
Sunday 4th July 2021 (stand out)
KORB Family Mixed Netball Carnival
Nice to have
• make the date stand out. We want people to lock in the date we're promoting.

```html
<!DOCTYPE html>
<html lang="en">
<head>
<meta charset="utf-8">
<title>Save the Date – KORB Family Mixed Netball Carnival</title>
<link href="https://fonts.googleapis.com/css2?family=Playball&family=Merriweather:wght@400;700;900&family=Oswald:wght@600&display=swap" rel="stylesheet">
<style>
  :root {
    --teal: #05a6b4;
    --teal-deep: #029aa8;
    --glow: #d3edf1;
    --yellow: #fcd116;
    --red: #e3202a;
    --ink: #111111;
    --white: #ffffff;
  }
  html, body {
    margin: 0;
    padding: 0;
    overflow: hidden;
    background: var(--teal);
  }
  .poster {
    position: relative;
    width: 884px;
    height: 1200px;
    overflow: hidden;
    background:
      radial-gradient(ellipse 340px 400px at 450px 790px, var(--glow) 0%, #7fd0d9 45%, rgba(5,166,180,0) 100%),
      linear-gradient(180deg, var(--teal) 0%, var(--teal-deep) 100%);
    font-family: "Merriweather", Georgia, serif;
    color: var(--white);
  }

  .ornament {
    position: absolute;
    pointer-events: none;
  }
  .ornament--top {
    right: 0;
    top: 10px;
    width: 200px;
    height: 190px;
    background: radial-gradient(ellipse at 60% 50%, rgba(255,255,255,0.14) 0%, rgba(255,255,255,0) 70%);
  }
  .ornament--bottom {
    left: 0;
    top: 830px;
    width: 230px;
    height: 230px;
    background: radial-gradient(ellipse at 40% 55%, rgba(255,255,255,0.13) 0%, rgba(255,255,255,0) 70%);
  }

  .brand {
    position: absolute;
    left: 36px;
    top: 40px;
    width: 150px;
    text-align: center;
  }
  .brand__mark {
    display: block;
    width: 60px;
    height: 60px;
    margin: 0 auto 30px;
    border-radius: 50%;
    background: var(--red);
  }
  .brand__name {
    font-family: "Oswald", "Arial Narrow", sans-serif;
    font-weight: 600;
    font-size: 13px;
    line-height: 1.25;
    letter-spacing: 0.3px;
    text-transform: uppercase;
    color: var(--ink);
  }

  .headline {
    position: absolute;
    left: 0;
    top: 0;
    width: 100%;
    margin: 0;
    font-family: "Playball", cursive;
    font-weight: 400;
    color: var(--white);
  }
  .headline__save {
    position: absolute;
    left: 178px;
    top: 140px;
    font-size: 205px;
    line-height: 1;
  }
  .headline__the {
    position: absolute;
    left: 174px;
    top: 320px;
    font-size: 78px;
    line-height: 1;
  }
  .headline__date {
    position: absolute;
    left: 300px;
    top: 275px;
    font-size: 205px;
    line-height: 1;
  }

  .date-band {
    position: absolute;
    left: 91px;
    top: 464px;
    width: 700px;
    height: 82px;
    background: var(--yellow);
    box-shadow: 0 16px 16px -12px rgba(0,0,0,0.4);
    display: flex;
    align-items: center;
    justify-content: center;
    gap: 6px;
    font-weight: 900;
    white-space: nowrap;
  }
  .date-band__day {
    color: var(--ink);
    font-size: 38px;
    padding-top: 6px;
  }
  .date-band__date {
    color: var(--red);
    font-size: 56px;
  }

  .campaign-art {
    position: absolute;
    left: 171px;
    top: 588px;
    width: 546px;
    height: 423px;
    border-radius: 60px;
    background: linear-gradient(160deg, var(--red) 0%, #1a1a1a 45%, var(--yellow) 100%);
  }

  .event {
    position: absolute;
    left: 0;
    top: 1060px;
    width: 100%;
    text-align: center;
    font-size: 30px;
    line-height: 1.2;
    font-weight: 400;
  }
  .event p { margin: 0; }

  .footer-band {
    position: absolute;
    left: 0;
    bottom: 0;
    width: 100%;
    height: 40px;
  }
</style>
</head>
<body>
<main class="poster">
  <div class="ornament ornament--top" role="img" aria-label="Faint decorative pattern of concentric rings and diagonal stripes"></div>
  <div class="ornament ornament--bottom" role="img" aria-label="Faint decorative pattern of concentric rings and diagonal stripes"></div>

  <header class="brand">
    <span class="brand__mark"></span>
    <div class="brand__name">Korb Community<br>Health Service</div>
  </header>

  <h1 class="headline">
    <span class="headline__save">Save</span>
    <span class="headline__the">The</span>
    <span class="headline__date">Date!</span>
  </h1>

  <div class="date-band">
    <span class="date-band__day">Sunday-</span>
    <span class="date-band__date">4th July 2021</span>
  </div>

  <div class="campaign-art" role="img" aria-label="Hand-lettered campaign slogan artwork in red and yellow with black outline"></div>

  <section class="event">
    <p>KORB Family Mixed Netball Carnival</p>
    <p>Nice to haveipsum</p>
  </section>

  <svg class="footer-band" viewBox="0 0 884 40" preserveAspectRatio="none" aria-hidden="true">
    <rect x="0" y="0" width="884" height="40" fill="#e3202a"/>
    <polygon points="772,0 780,0 800,40 792,40" fill="#05a6b4"/>
  </svg>
</main>
</body>
</html>
```